Roof Plumbing Company needs simple, modern business card using the attached logo and below details:

Dean Halloway
Summit Gutters Pty Ltd
ABN: 58 214 937 062
Phone: 0417 286 531
Email: summitgutters@mailbrook.com
Website: summitgutters.com.au

For all of your metal roof plumbing requirements contact Summit Gutters for an obligation free quote - no job too big or to small!

Industry/Entity Type

Business

Contact Information for Business Card

Dean Halloway
Summit Gutters Pty Ltd
ABN 58 214 937 062
0417 286 531
summitgutters@mailbrook.com
summitgutters.com.au

Requirements
Must have
• Bright eye catching design, professional look

```html
<!DOCTYPE html>
<html lang="en">
<head>
<meta charset="utf-8">
<title>Summit Gutters – Business Card</title>
<link href="https://fonts.googleapis.com/css2?family=Montserrat:ital,wght@0,400;0,500;0,700;0,800;1,400&display=swap" rel="stylesheet">
<style>
  :root {
    --backdrop: #2f4049;
    --card: #ffffff;
    --brand-red: #c4161c;
    --band-red: #b01c22;
    --ink: #1b1b1b;
    --muted: #6b6b6b;
    --band-dark: #1a1a1a;
  }
  * { margin: 0; padding: 0; box-sizing: border-box; }
  html, body {
    width: 1200px; height: 1200px; overflow: hidden;
    background: var(--backdrop);
    font-family: "Montserrat", Arial, sans-serif;
  }
  .business-card {
    position: absolute; left: 100px; top: 314px;
    width: 1000px; height: 571px;
    background: var(--card);
    overflow: hidden;
    color: var(--ink);
  }
  .brand-name {
    position: absolute; left: 90px; top: 215px;
    font-weight: 800; font-size: 54px; letter-spacing: 1px;
    color: var(--brand-red);
  }
  .contact-block { position: absolute; left: 610px; top: 168px; }
  .person-name { font-weight: 700; font-size: 38px; color: var(--brand-red); }
  .person-role { font-size: 19px; color: var(--muted); margin-top: 6px; }
  .contact-list { list-style: none; margin-top: 22px; }
  .contact-list li {
    display: flex; align-items: center; gap: 14px;
    font-size: 21px; line-height: 37px; letter-spacing: 0.5px;
  }
  .contact-list svg { width: 22px; height: 22px; flex: none; fill: var(--ink); }
  .company-block { position: absolute; left: 80px; top: 428px; }
  .company-name { font-weight: 700; font-style: italic; font-size: 28px; }
  .company-abn { font-style: italic; font-size: 19px; color: var(--muted); margin-top: 4px; letter-spacing: 0.5px; }
  .address-block {
    position: absolute; left: 612px; top: 418px;
    font-size: 29px; line-height: 42px; letter-spacing: 0.5px; color: #2a2a2a;
  }
  .footer-band { position: absolute; left: 0; bottom: 0; width: 1000px; height: 52px; }
</style>
</head>
<body>
  <div class="business-card">
    <div class="brand-name">Summit Gutters</div>

    <div class="contact-block">
      <div class="person-name">Dean Halloway</div>
      <div class="person-role">Position</div>
      <ul class="contact-list">
        <li>
          <svg viewBox="0 0 24 24" aria-hidden="true"><rect x="1" y="1" width="22" height="22" rx="4"/><path d="M8 5.5l2 3-1.3 1.5c.9 1.9 2.4 3.4 4.3 4.3l1.5-1.3 3 2-1 2.5c-5.5-.3-10-4.8-10.3-10.3z" fill="#fff"/></svg>
          0417 286 531
        </li>
        <li>
          <svg viewBox="0 0 24 24" aria-hidden="true"><path d="M1 5h22v14H1z"/><path d="M2.5 6.5L12 13l9.5-6.5" stroke="#fff" stroke-width="2" fill="none"/></svg>
          summitgutters@mailbrook.com
        </li>
        <li>
          <svg viewBox="0 0 24 24" aria-hidden="true"><path d="M12 2L0 12h3v10h7v-6h4v6h7V12h3z"/></svg>
          summitgutters.com.au
        </li>
      </ul>
    </div>

    <div class="company-block">
      <div class="company-name">Summit Gutters Pty Ltd</div>
      <div class="company-abn">ABN 58 214 937 062</div>
    </div>

    <div class="address-block">Address Street<br>City State Zip Code</div>

    <svg class="footer-band" viewBox="0 0 1000 52" preserveAspectRatio="none" aria-hidden="true">
      <rect width="1000" height="52" fill="var(--band-dark)"/>
      <polygon points="0,0 382,0 400,52 0,52" fill="var(--band-red)"/>
      <polygon points="265,0 274,0 286,52 277,52" fill="#fff"/>
      <polygon points="382,0 392,0 410,52 400,52" fill="#fff"/>
    </svg>
  </div>
</body>
</html>
```